Flyer for Corvane Visual - Design Agency

We need a 4-page square flyer measuring 14.8x14.8cm per page, to fold out, for a design agency targeting small businesses.
The design should be very modern. There shouldn't be too much content visible.
The background should be black. The color of the logo (attached) can also be used. The content is also attached and divided per page. We are open to alternative suggestions regarding the division.

```html
<!DOCTYPE html>
<html lang="de">
<head>
<meta charset="utf-8">
<title>Corvane Visual – Flyer</title>
<link href="https://fonts.googleapis.com/css2?family=Quicksand:wght@300;400;500;600;700&display=swap" rel="stylesheet">
<style>
  :root {
    --stage: #e4e4e2;
    --ink-black: #0b0b0b;
    --ink-charcoal: #2e2e2e;
    --ink-grey: #3a3a3a;
    --text-light: #e8e8e8;
    --text-muted: #9a9a9a;
    --teal: #5fd8cf;
    --blue: #1c8fe0;
    --pink: #e23a9b;
    --line-white: #d9d9d9;
  }
  * { box-sizing: border-box; margin: 0; padding: 0; }
  html, body { width: 1200px; height: 487px; overflow: hidden; }
  body {
    background: var(--stage);
    font-family: "Quicksand", sans-serif;
    position: relative;
  }
  .spread {
    position: absolute;
    top: 101px;
    width: 570px;
    height: 285px;
    display: flex;
  }
  .spread--outside { left: 15px; }
  .spread--inside { left: 615px; }
  .page {
    width: 285px;
    height: 285px;
    position: relative;
    overflow: hidden;
  }
  .page--charcoal { background: var(--ink-charcoal); }
  .page--black { background: var(--ink-black); }
  .page--grey { background: var(--ink-grey); }

  /* back cover */
  .wordmark { color: var(--teal); font-weight: 600; line-height: 1; }
  .back .wordmark { position: absolute; left: 26px; top: 30px; font-size: 20px; }
  .back .claim {
    position: absolute; left: 26px; top: 72px;
    color: var(--text-light); font-size: 15px; font-weight: 500; line-height: 1.3;
  }
  .back .cta {
    position: absolute; left: 26px; top: 130px;
    color: var(--blue); font-size: 9.5px; font-weight: 500;
    letter-spacing: 0.04em; line-height: 1.4; text-transform: uppercase;
  }
  .back .contact {
    position: absolute; left: 26px; top: 178px;
    font-size: 8.5px; line-height: 1.55; color: var(--text-light); list-style: none;
  }
  .back .contact .address { color: var(--blue); }
  .back .owners {
    position: absolute; left: 26px; top: 252px;
    font-size: 6.5px; color: var(--text-muted);
  }

  /* front cover */
  .front .tagline {
    position: absolute; right: 26px; top: 28px; text-align: right;
    font-size: 10px; line-height: 1.4; color: var(--text-light);
  }
  .front .tagline .t1 { color: var(--blue); }
  .front .tagline .t2 { color: var(--teal); }
  .front .tagline b { font-weight: 700; }
  .front .wordmark {
    position: absolute; left: 26px; bottom: 34px;
    font-size: 42px; line-height: 0.95;
  }

  /* inside left */
  .mmm {
    position: absolute; left: 22px; top: 28px;
    font-size: 25px; font-weight: 300; letter-spacing: 0.04em; line-height: 1.12;
  }
  .mmm span { display: block; }
  .mmm .m1 { color: var(--text-light); }
  .mmm .m2 { color: var(--teal); }
  .mmm .m3 { color: var(--blue); }
  .mission {
    position: absolute; left: 22px; top: 158px; display: flex; gap: 10px; align-items: center;
  }
  .mission .wordmark { font-size: 14px; line-height: 1.05; }
  .mission p { color: var(--teal); font-size: 7.5px; line-height: 1.35; max-width: 130px; opacity: 0.85; }
  .intro {
    position: absolute; left: 22px; top: 212px; max-width: 200px;
    color: var(--text-light); font-size: 8px; line-height: 1.45;
  }

  /* inside right */
  .services { position: absolute; left: 20px; top: 24px; right: 22px; }
  .section-title {
    color: var(--text-light); font-size: 9px; font-weight: 700;
    letter-spacing: 0.05em; text-transform: uppercase; margin-bottom: 7px;
  }
  .service { display: flex; gap: 8px; margin-bottom: 7px; }
  .service svg { flex: none; margin-top: 2px; }
  .service h3 {
    color: var(--pink); font-size: 8.5px; font-weight: 600;
    text-transform: uppercase; letter-spacing: 0.03em;
  }
  .service p { color: var(--text-light); font-size: 6.5px; line-height: 1.35; opacity: 0.85; }
  .why { position: absolute; left: 20px; top: 196px; right: 22px; }
  .why ul { list-style: none; }
  .why li {
    color: var(--text-light); font-size: 6.5px; line-height: 1.4; opacity: 0.85;
    padding-left: 8px; position: relative; margin-bottom: 3px;
  }
  .why li::before {
    content: ""; position: absolute; left: 0; top: 3px;
    width: 3px; height: 3px; border-radius: 50%; background: var(--pink);
  }

  .frame-lines { position: absolute; inset: 0; pointer-events: none; }
</style>
</head>
<body>

<section class="spread spread--outside" aria-label="Außenseite">
  <div class="page page--charcoal back">
    <div class="wordmark">Corvane Visual</div>
    <p class="claim">Designs, die wirken.<br>Marken, die bleiben.</p>
    <p class="cta">Kontaktiere uns für eine<br>kostenlose Beratung!</p>
    <ul class="contact">
      <li>design@corvanevisual.de</li>
      <li>+49 000 48213</li>
      <li class="address">Weidenweg 24</li>
      <li class="address">60487 Frankfurt</li>
    </ul>
    <p class="owners">Inhaber: Lena Ostrow &amp; Tim Faber</p>
  </div>
  <div class="page page--black front">
    <p class="tagline">
      <span class="t1">Unser <b>Design.</b></span><br>
      <span class="t2">Dein <b>Stil.</b></span><br>
      Dein <b>Unternehmen.</b>
    </p>
    <div class="wordmark">Corvane<br>Visual</div>
  </div>
</section>

<section class="spread spread--inside" aria-label="Innenseite">
  <div class="page page--black">
    <h1 class="mmm"><span class="m1">MODERN</span><span class="m2">MUTIG</span><span class="m3">MARKANT</span></h1>
    <div class="mission">
      <div class="wordmark">Corvane<br>Visual</div>
      <p>gestaltet die Zukunft deines Unternehmensauftritts.</p>
    </div>
    <p class="intro">Wir machen aus Ideen visuelle Erlebnisse und sorgen dafür, dass deine Marke im Gedächtnis bleibt.</p>
  </div>
  <div class="page page--grey">
    <div class="services">
      <h2 class="section-title">Unsere Leistungen:</h2>
      <div class="service">
        <svg width="12" height="12" viewBox="0 0 12 12"><path d="M6 1 L8 5 L8 9 L4 9 L4 5 Z M4 9 L3 11 M8 9 L9 11" fill="none" stroke="#e8e8e8" stroke-width="0.8"/></svg>
        <div><h3>Next-Level Flyer</h3><p>Nicht nur Papier, sondern deine Botschaft im perfekten Look.</p></div>
      </div>
      <div class="service">
        <svg width="12" height="12" viewBox="0 0 12 12"><circle cx="6" cy="6" r="5" fill="none" stroke="#e8e8e8" stroke-width="0.8"/><circle cx="4" cy="5" r="0.9" fill="#e8e8e8"/><circle cx="7" cy="4" r="0.9" fill="#e8e8e8"/></svg>
        <div><h3>Corporate Identity</h3><p>Ein Design, das deine Marke spricht – individuell, stark, unvergesslich.</p></div>
      </div>
      <div class="service">
        <svg width="12" height="12" viewBox="0 0 12 12" fill="none" stroke="#e8e8e8" stroke-width="0.8"><circle cx="6" cy="6" r="5"/><ellipse cx="6" cy="6" rx="2.2" ry="5"/><path d="M1 6 H11 M2 3.5 H10 M2 8.5 H10"/></svg>
        <div><h3>Digital &amp; Print</h3><p>Ob Social Media Grafiken oder klassisches Printdesign – wir sind da, wo du uns brauchst.</p></div>
      </div>
      <div class="service">
        <svg width="12" height="12" viewBox="0 0 12 12"><path d="M6 1 L7.3 4.4 L11 4.6 L8.1 6.9 L9.1 10.5 L6 8.5 L2.9 10.5 L3.9 6.9 L1 4.6 L4.7 4.4 Z" fill="none" stroke="#e8e8e8" stroke-width="0.8"/></svg>
        <div><h3>Alles aus einer Hand</h3><p>Logo, Farben, Typografie, Flyer und vieles mehr – wir bauen das Fundament für deinen Erfolg.</p></div>
      </div>
    </div>
    <div class="why">
      <h2 class="section-title">Warum wir?</h2>
      <ul>
        <li>Dein Style, unser Know-how: Wir kombinieren deine Vision mit moderner Ästhetik.</li>
        <li>Persönlicher Service – Wir hören zu und setzen um, was dich einzigartig macht.</li>
        <li>Flexible Lösungen für die unterschiedlichsten Anforderungen.</li>
      </ul>
    </div>
  </div>
  <svg class="frame-lines" viewBox="0 0 570 285" aria-hidden="true" fill="none" stroke-width="0.8">
    <path d="M150 47 H300 V278" stroke="var(--line-white)"/>
    <path d="M112 75 H288 V278" stroke="var(--teal)"/>
    <path d="M160 103 H276 V278 H560" stroke="var(--blue)"/>
    <path d="M560 12 V150 H470" stroke="var(--pink)"/>
  </svg>
</section>

</body>
</html>
```